Find Bright Harbor Business Card and logo

We need a logo design and business card for a new consulting firm called Find Bright Harbor. We specialize in Digital Transformation of enterprises of all sizes. We help enterprises understand & significantly increase their business velocity. This requires changes in culture, organization, process and technology. We also partner with advanced technology companies to deliver tangible accelerated solutions. Methods utilized include Agile, Design Thinking, Advanced Technology Platforms (microservices, digital data, virtualization, blockchain, etc.). The final design should communicate velocity, transformation, growth and innovation.

Target Market(s)

Large Corporations and Enterprises

Contact Information for Business Card

Tagline - Shape the Coming

Logo Text

Find Bright Harbor or an initial or initials or a symbol/picture

Requirements
Must have
• Front side: Logo, name of business (Find Bright Harbor), tagline (Shape the Coming)
• Back side: First Name, Last Name, Title, Mobile Phone, Email, LinkedIn, URL (findbrightharbor.com)
Nice to have
• The design should communicate velocity, transformation, growth and/or innovation.

```html
<!DOCTYPE html>
<html lang="en">
<head>
<meta charset="utf-8">
<title>Find Bright Harbor — Business Card</title>
<link rel="stylesheet" href="https://fonts.googleapis.com/css2?family=Michroma&family=Montserrat:wght@500;600&display=swap">
<style>
  :root {
    --stage: #1c1c1e;
    --card-dark: #0b0b0c;
    --card-light: #ffffff;
    --navy: #2e2f9a;
    --periwinkle: #8e92db;
    --red: #e8262b;
    --orange: #f5821f;
    --yellow: #f7e21b;
    --grey: #8a8a8a;
    --ink: #141414;
  }
  * { box-sizing: border-box; margin: 0; padding: 0; }
  html, body { width: 1200px; height: 1200px; overflow: hidden; }
  body {
    background: var(--stage);
    font-family: "Montserrat", sans-serif;
    position: relative;
  }
  .card {
    position: absolute;
    left: 150px;
    width: 900px;
    height: 514px;
    border-radius: 28px;
    overflow: hidden;
  }
  .card--front { top: 60px; background: var(--card-dark); }
  .card--back { top: 626px; background: var(--card-light); }

  .brand {
    position: absolute;
    display: flex;
    flex-direction: column;
    align-items: flex-end;
  }
  .brand__row { display: flex; align-items: center; gap: 14px; }
  .brand__mark { width: 22px; height: 22px; background: var(--orange); }
  .brand__name {
    font-family: "Michroma", sans-serif;
    font-size: 40px;
    letter-spacing: 1px;
    text-transform: uppercase;
    white-space: nowrap;
  }
  .brand__tagline {
    font-family: "Michroma", sans-serif;
    font-size: 18px;
    letter-spacing: 3px;
    text-transform: uppercase;
    color: var(--grey);
    margin-top: 14px;
  }
  .card--front .brand { left: 0; right: 0; top: 200px; align-items: center; }
  .card--front .brand__name { color: var(--periwinkle); }
  .card--front .brand__tagline { align-self: center; }

  .card--back .brand { right: 50px; top: 150px; }
  .card--back .brand__name { color: var(--navy); font-size: 32px; }
  .card--back .brand__tagline { font-size: 15px; }

  .accent-bar {
    position: absolute; left: 0; top: 70px;
    width: 24px; height: 46px; background: var(--navy);
  }
  .person { position: absolute; left: 58px; top: 68px; }
  .person__name {
    font-family: "Michroma", sans-serif;
    font-size: 30px; color: var(--navy); letter-spacing: 1px;
  }
  .person__title {
    font-family: "Michroma", sans-serif;
    font-size: 19px; color: var(--red); margin-top: 6px;
  }

  .divider {
    position: absolute; left: 58px; top: 278px;
  }

  .contacts {
    position: absolute; left: 58px; top: 308px;
    list-style: none;
  }
  .contacts li {
    display: flex; align-items: center; gap: 16px;
    font-size: 22px; font-weight: 500; color: var(--ink);
    height: 40px;
  }
  .contacts .icon {
    width: 26px; height: 26px; border-radius: 5px;
    background: var(--red);
    display: flex; align-items: center; justify-content: center;
  }

  .pixel-field {
    position: absolute; right: 0; bottom: 0;
    width: 420px; height: 220px;
    background: radial-gradient(ellipse at 85% 80%, rgba(46,47,154,0.35), rgba(245,130,31,0.18) 45%, rgba(255,255,255,0) 75%);
  }
</style>
</head>
<body>

<section class="card card--front">
  <div class="brand">
    <div class="brand__row">
      <span class="brand__mark"></span>
      <span class="brand__name">Find Bright Harbor</span>
    </div>
    <span class="brand__tagline">Shape the Coming</span>
  </div>
</section>

<section class="card card--back">
  <span class="accent-bar"></span>
  <div class="person">
    <div class="person__name">DANIEL REYES</div>
    <div class="person__title">Managing Director</div>
  </div>

  <div class="brand">
    <div class="brand__row">
      <span class="brand__mark"></span>
      <span class="brand__name">Find Bright Harbor</span>
    </div>
    <span class="brand__tagline">Shape the Coming</span>
  </div>

  <svg class="divider" width="820" height="20" viewBox="0 0 820 20">
    <line x1="0" y1="10" x2="804" y2="10" stroke="#2e2f9a" stroke-width="2"/>
    <circle cx="810" cy="10" r="7" fill="#fff" stroke="#2e2f9a" stroke-width="2.5"/>
  </svg>

  <ul class="contacts">
    <li>
      <span class="icon">
        <svg width="14" height="18" viewBox="0 0 14 18"><rect x="1.5" y="1" width="11" height="16" rx="2" fill="none" stroke="#fff" stroke-width="1.8"/><circle cx="7" cy="14" r="1.2" fill="#fff"/></svg>
      </span>
      555-014-2278
    </li>
    <li>
      <span class="icon">
        <svg width="18" height="14" viewBox="0 0 18 14"><rect x="1" y="1" width="16" height="12" fill="none" stroke="#fff" stroke-width="1.6"/><polyline points="1,1 9,8 17,1" fill="none" stroke="#fff" stroke-width="1.6"/></svg>
      </span>
      info@findbrightharbor.com
    </li>
    <li>
      <span class="icon"></span>
      findbrightharbor
    </li>
    <li>
      <span class="icon">
        <svg width="18" height="18" viewBox="0 0 18 18" fill="none" stroke="#fff" stroke-width="1.4"><circle cx="9" cy="9" r="7.5"/><ellipse cx="9" cy="9" rx="3.5" ry="7.5"/><line x1="1.5" y1="9" x2="16.5" y2="9"/></svg>
      </span>
      findbrightharbor.com
    </li>
  </ul>

  <div class="pixel-field" role="img" aria-label="Scattered pixel squares in navy, red, orange and yellow"></div>
</section>

</body>
</html>
```